Broschüre für Premium Kunstrasen
Zielgruppe
Hauptsächlich (70% unserer Tätigkeit) verlegen wir Premium Kunstrasen in Gärten von Privatleuten. Schlüsselfertig .
Unsere Auftraggeber in diesem Bereich sind in der Regel zwischen 35 bis 70 Jahre alt und gut situiert.
30% unserer Tätigkeit besteht aus der Lieferung von hochwertigen Kunstrasen für den Balkon, Terrasse.
Unsere Produkte haben lange Garantiezeiten von 15 Jahren. Deshalb nennen wir unsere Produkte auch Sonnhalm
Aufgabenstellung
Textvorgaben und Headlines kommen von uns

```html
<!DOCTYPE html>
<html lang="de">
<head>
<meta charset="utf-8">
<title>Kunstrasen selbst verlegen – Broschüre</title>
<link href="https://fonts.googleapis.com/css2?family=Archivo:wght@400;500;700;800&family=Fira+Sans:wght@400;600&display=swap" rel="stylesheet">
<style>
  :root {
    --bg: #d2d2d2;
    --paper: #ececea;
    --paper-right: #eeeeec;
    --green-dark: #2a5a2a;
    --green-head: #1f4f1f;
    --lime: #b8d96a;
    --lime-line: #a6c51c;
    --ink: #1d1d1d;
    --white: #ffffff;
  }
  * { margin: 0; padding: 0; box-sizing: border-box; }
  html, body { width: 1200px; height: 1200px; overflow: hidden; }
  body { background: var(--bg); font-family: "Archivo", sans-serif; color: var(--ink); position: relative; }

  .spread { position: absolute; left: 44px; top: 306px; width: 1112px; height: 588px; display: flex; box-shadow: 0 14px 30px rgba(0,0,0,.18); }
  .page { position: relative; width: 556px; height: 100%; overflow: hidden; }
  .page--left { background: var(--paper); }
  .page--right { background: var(--paper-right); display: flex; }

  .intro { position: absolute; left: 0; top: 0; width: 305px; height: 100%; }
  .intro__bar { position: absolute; left: 56px; top: 94px; width: 61px; height: 4px; background: var(--green-head); }
  .intro__title { position: absolute; left: 56px; top: 108px; font-size: 25px; font-weight: 700; line-height: 1.32; color: var(--green-head); letter-spacing: -0.2px; }
  .intro__text { position: absolute; left: 58px; top: 196px; width: 212px; font-size: 10.4px; line-height: 15.7px; letter-spacing: -0.2px; }
  .intro__text p + p { margin-top: 7px; }
  .intro__corner { position: absolute; left: 50px; top: 483px; width: 208px; height: 67px; border-left: 3px solid var(--lime-line); border-bottom: 3px solid var(--lime-line); }

  .hero { position: absolute; left: 305px; top: 0; width: 251px; height: 100%;
    background: linear-gradient(180deg, #3f8fd6 0%, #5aaee0 40%, #7ab0c8 58%, #6b8a5a 72%, #4f9a3a 82%, #3f8a2c 100%); }
  .hero__frame { position: absolute; left: 66px; top: 120px; width: 131px; height: 146px; border-top: 3px solid var(--lime-line); border-right: 3px solid var(--lime-line); }
  .hero__frame::before { content: ""; position: absolute; left: 0; top: 0; width: 3px; height: 33px; background: var(--lime-line); }
  .hero__frame::after { content: ""; position: absolute; right: -3px; bottom: -3px; width: 18px; height: 3px; background: var(--lime-line); }
  .hero__title { position: absolute; left: 0; top: 176px; width: 186px; text-align: center; font-size: 24px; font-weight: 800; color: var(--white); }
  .hero__sub { position: absolute; left: 0; top: 210px; width: 192px; text-align: center; font-size: 14px; font-weight: 700; color: var(--white); }

  .technique { position: relative; width: 324px; height: 100%; }
  .technique__title { position: absolute; left: 50px; top: 52px; width: 230px; font-size: 19px; font-weight: 700; line-height: 25px; color: var(--green-head); }
  .technique__text { position: absolute; left: 50px; top: 138px; width: 226px; font-size: 10.4px; line-height: 15.8px; letter-spacing: -0.1px; }
  .technique__text p + p { margin-top: 8px; }

  .benefits { width: 232px; height: 100%; display: flex; flex-direction: column; font-family: "Fira Sans", sans-serif; }
  .benefit { position: relative; padding: 0 18px 0 27px; color: var(--white); }
  .benefit--dark { background: var(--green-dark); }
  .benefit--light { background: var(--lime); color: var(--green-head); }
  .benefit:nth-child(1) { height: 204px; padding-top: 37px; }
  .benefit:nth-child(2) { height: 185px; padding-top: 32px; }
  .benefit:nth-child(3) { flex: 1; padding-top: 34px; }
  .benefit__title { font-family: "Archivo", sans-serif; font-size: 17.5px; font-weight: 700; line-height: 21px; width: 130px; }
  .benefit__text { margin-top: 6px; font-size: 11.6px; line-height: 17px; }
  .benefit__icon { position: absolute; right: 20px; top: 14px; width: 56px; height: 60px; }
</style>
</head>
<body>
<main class="spread">
  <section class="page page--left">
    <div class="intro">
      <span class="intro__bar"></span>
      <h1 class="intro__title">Kunstrasen<br>selbst verlegen</h1>
      <div class="intro__text">
        <p>Wenn Sie unsere Kunstrasen selbst verlegen möchten, verraten wir ihnen, auf was es ankommt und geben Ihnen Schritt für Schritt Hilfestellung - damit ihr Kunstrasen perfekt verlegt werden kann.</p>
        <p>Bevor Sie Kunstrasen selbst verlegen, muss der Untergrund optimal vorbereitet werden. Sie sollten also schon etwas handwerklich geübt sein, um später ein perfektes Aussehen der Fläche zu erreichen.</p>
        <p>Aber auch das passgenaue Verlegen des Kunstrasens ist nicht unbedingt ein Kinderspiel. Wenn Sie sich nicht wirklich sicher sind, dass Sie Kunstrasen selbst verlegen können oder nicht die Geduld für eine derartige Aufgabe aufbringen, sollten Sie lieber einen Profi beauftragen.</p>
      </div>
      <span class="intro__corner"></span>
    </div>
    <div class="hero" role="img" aria-label="Foto: Haus mit Fachwerkgiebel hinter Büschen und einem gepflegten grünen Kunstrasen unter blauem Himmel">
      <span class="hero__frame"></span>
      <p class="hero__title">Sorgenfrei.</p>
      <p class="hero__sub">Dank Rasenwerk Lindner</p>
    </div>
  </section>

  <section class="page page--right">
    <div class="technique">
      <h2 class="technique__title">Kunstrasenverlegung: Auf die Technik kommt es an</h2>
      <div class="technique__text">
        <p>Sicherlich ist die Schwierigkeit beim Kunstrasen verlegen stark abhängig von der Größe der Fläche. Eine eher kleine und rechteckige Fläche ohne Bewuchs ist für einen Laien auf jeden Fall machbar. Stehen aber noch Bäume oder Büsche auf der Fläche? Dann wird nicht nur das Schneiden, sondern auch das Zusammensetzen von Kunstrasenbahnen zur echten Herausforderung.</p>
        <p>Der erste Schritt ist die Vorbereitung des Untergrundes. Er muss eben, stabil und wasserdurchlässig sein. Nur ein Untergrund mit Schotter beschert ihnen Ergebnisse über die Sie sich Jahrzehnte freuen werden.</p>
        <p>Wenn ihre Fläche aus mehreren Bahnen besteht, legen Sie den Kunstrasen an den Seiten gerade an. Bevor Sie den Kunstrasen final zuschneiden, achten Sie bitte darauf, dass die Stöße gut anliegen. Verwenden Sie zum Schneiden ein scharfes Teppichmesser und schneiden Sie immer auf der Rückseite des Kunstrasens. So verhindern Sie, dass die Grasfasern durchtrennt werden. Die Bahnen werden mit einem Kaltnahtband zusammengefügt (verschweisst).</p>
      </div>
    </div>

    <aside class="benefits">
      <div class="benefit benefit--dark">
        <svg class="benefit__icon" viewBox="0 0 56 60" fill="none" stroke="#b8d96a" stroke-width="1.6">
          <path d="M3 56V2h50v14"/>
          <circle cx="32" cy="28" r="14"/>
          <circle cx="32" cy="28" r="9"/>
          <path d="M28 28l3 3 5-6"/>
          <path d="M25 40l-5 13 5-3 3 5 4-12M39 40l5 13-5-3-3 5-4-12"/>
          <path d="M3 56h6"/>
        </svg>
        <h3 class="benefit__title">Qualifizierte Beratung</h3>
        <p class="benefit__text">Bevor Sie Kunstrasen selbst verlegen, bieten wir Ihnen vorab eine qualifizierte Beratung. Nutzen Sie unsere Tricks &amp; Kniffe für wundervoll aussehende Kunstrasenflächen.</p>
      </div>
      <div class="benefit benefit--light">
        <svg class="benefit__icon" viewBox="0 0 56 60" fill="none" stroke="#1f4f1f" stroke-width="1.6">
          <path d="M3 50V2h46v10"/>
          <circle cx="33" cy="34" r="18"/>
          <circle cx="33" cy="34" r="13"/>
          <path d="M33 26v8l6 4"/>
          <path d="M3 50h6"/>
        </svg>
        <h3 class="benefit__title">Perfekter Projektablauf</h3>
        <p class="benefit__text">Ein dauerhaft gut aussehender Kunstrasen benötigt einen optimalen Untergrund. Laden Sie bei Bedarf unsere Verlege- und Installationsanleitung herunter.</p>
      </div>
      <div class="benefit benefit--dark">
        <svg class="benefit__icon" viewBox="0 0 56 60" fill="none" stroke="#b8d96a" stroke-width="1.6">
          <path d="M3 56V2h50v10"/>
          <path d="M16 22h20v6H16zM24 28v26h5V28"/>
          <path d="M44 16v14M40 30h8v6h-8zM44 36v12"/>
          <circle cx="44" cy="51" r="3"/>
          <path d="M3 56h6"/>
        </svg>
        <h3 class="benefit__title">11 Jahre Erfahrung</h3>
        <p class="benefit__text">Mit dem Wissen aus hunderten Projekten schaffen wir gemeinsam Flächen, um die Sie ihre Freunde und Bekannte beneiden werden.</p>
      </div>
    </aside>
  </section>
</main>
</body>
</html>
```